Bright and vibrant Jewelry Designer Web Page

Hi creative artists,

My name is Marta, I'm a local jewelry designer with a small store in Duesseldorf Germany. All my Jewelrys are unique and hand crafted by my self.

My designs are colorful, young, modern and trendy as well as timeless and durable due to the high quality materials. I use gold, silver, jewelry, fresh water pearls and hand crafted glass.

Competitors are local goldsmith which produce custom-made jewelry.

I have started my business with my jewelry label "twigs and ribbons" 2007:
http://www.twigs-and-ribbons.de/start.php

In 2009 I have opened my store "Kupfer und Leinen" (silver and silk) together with a fashion designer:
http://www.kupfer-leinen.de/home.php
https://www.facebook.com/Kupfer.und.Leinen (latest jewelrys)

Scope of pages:
● welcome page
● category overview
- short introduction
- sub categories: Earring, Necklace, Ring, Bride Jewelry, ...
● category page
- short introduction
- products of this category
● product page
- short introduction
- about 3 to 4 pictures
- description: materials, dimensions
- price
- ! important ! related products
● contact page
- address
- contact form
● blog
- picture
- text

Conclusion:
● We need a emotional page
● Lots of impressive and brilliant product images
● A feminine touch
● Last but not least the design should reflect
- outstanding design
- uniqueness
- made-to-measure

Target Market(s)

Women in the mid 20's and 30's , interested in individual style, fashion and luxury goods

Industry/Entity Type

Jewelry

Requirements
Must have
• ● css for screen, mobile devices and print
● full function also with out JavaScript
● only use free available fonts e.g. Lumora Type Library (http://www.lumoratype.example/webfonts)
Should not have
• ● sound
● flash

```html
<!DOCTYPE html>
<html lang="de">
<head>
<meta charset="utf-8">
<title>Kupfer und Leinen – Mode &amp; Schmuckdesign</title>
<link rel="stylesheet" href="https://fonts.googleapis.com/css2?family=Cinzel:wght@400&family=Josefin+Sans:wght@400;600&family=Open+Sans:wght@400;600&family=PT+Sans+Narrow:wght@400;700&family=Playfair+Display:wght@400&family=Lora:wght@700&display=swap">
<style>
  :root {
    --pink: #d9748d;
    --pink-soft: #ecc7d1;
    --ink: #3b3b3b;
    --text: #707070;
    --muted: #9a9a9a;
    --line: #d6d6d6;
    --panel: #ececec;
    --white: #ffffff;
    --black: #1e1e1e;
  }
  * { box-sizing: border-box; margin: 0; padding: 0; }
  html, body { width: 933px; height: 1200px; overflow: hidden; }
  body { position: relative; background: var(--white); font-family: "Open Sans", sans-serif; color: var(--text); }
  a { color: inherit; text-decoration: none; }
  .abs { position: absolute; }

  /* header */
  .top-band { left: 0; top: 0; width: 933px; height: 60px; background: linear-gradient(#f1f1f1, #e4e4e4); }
  .logo-panel { left: 260px; top: 0; width: 413px; height: 128px; }
  .brand { left: 267px; top: 24px; width: 386px; text-align: center; font-family: "Playfair Display", serif; font-size: 38px; color: #8e8e8e; letter-spacing: .5px; }
  .brand-dot { left: 322px; top: 80px; width: 24px; height: 24px; border-radius: 50%; background: var(--pink); }
  .social { display: flex; gap: 4px; }
  .social span { width: 21px; height: 21px; border-radius: 50%; background: #8a8a8a; }
  .social-top { left: 729px; top: 60px; }

  /* nav */
  .nav { left: 157px; top: 129px; width: 599px; height: 40px; }
  .nav ul { position: absolute; left: 32px; top: 0; height: 40px; display: flex; list-style: none; gap: 24px; align-items: center; }
  .nav li { font-family: "PT Sans Narrow", sans-serif; font-size: 15px; color: #6a6a6a; letter-spacing: .2px; position: relative; }
  .nav li.active { color: var(--pink); }
  .nav li.active::before { content: ""; position: absolute; left: -4px; right: -4px; top: -13px; height: 2px; background: var(--pink); }

  /* slider */
  .slider { left: 133px; top: 189px; width: 667px; height: 359px; border: 1px solid var(--line); overflow: hidden; }
  .slide-photo { position: absolute; inset: 0; background: linear-gradient(90deg, #efe9e7 0%, #e2d4d2 28%, #f3f3f5 45%, #d98b9c 62%, #f1f1f3 75%, #d7899a 88%, #eeeef0 100%); }
  .slide-head { position: absolute; left: 110px; top: 8px; width: 520px; text-align: center; white-space: nowrap; }
  .slide-head .line { font-family: "Cinzel", serif; font-size: 18px; line-height: 23px; color: #6d6d6d; }
  .slide-head .claim { font-family: "PT Sans Narrow", sans-serif; font-size: 31px; color: var(--pink); margin-top: 4px; letter-spacing: .5px; }
  .slide-arrow { position: absolute; top: 346px; width: 22px; height: 48px; }
  .slide-arrow.prev { left: 128px; }
  .slide-arrow.next { left: 784px; }
  .dots { left: 438px; top: 531px; width: 72px; height: 17px; background: var(--pink); border-radius: 3px 3px 0 0; display: flex; gap: 4px; justify-content: center; align-items: center; }
  .dots span { width: 8px; height: 8px; background: #f6dbe2; }
  .dots span:first-child { background: var(--white); }

  /* sidebar */
  .sidebar { left: 137px; top: 569px; width: 156px; height: 300px; background: var(--panel); }
  .box-head { height: 19px; display: flex; justify-content: space-between; align-items: center; padding: 2px 4px 0 9px; font-family: "Josefin Sans", sans-serif; font-size: 14px; letter-spacing: 1.5px; line-height: 1; }
  .box-head i { width: 13px; height: 13px; display: grid; place-items: center; margin-top: -2px; }
  .box-head.dark { background: #4a4a4a; color: var(--white); }
  .box-head.dark i { background: var(--white); }
  .box-head.light { background: var(--pink-soft); color: var(--ink); }
  .box-head.light i { background: #4a4a4a; }
  .cat-group { padding: 10px 6px 0 13px; }
  .cat-group h4 { font-size: 10px; font-weight: 600; color: #555; margin-bottom: 2px; }
  .cat-group li { list-style: none; font-size: 9.5px; line-height: 13.4px; color: #8a8a8a; padding-left: 9px; border-bottom: 1px solid #d2d2d2; }

  /* intro */
  .intro-head { left: 313px; top: 572px; width: 472px; display: flex; gap: 12px; align-items: flex-start; }
  .intro-title { font-family: "Josefin Sans", sans-serif; font-weight: 400; font-size: 17px; letter-spacing: .5px; color: var(--ink); white-space: nowrap; line-height: 22px; }
  .intro-lead { flex: 1; font-size: 9.5px; line-height: 17px; color: #555; padding-top: 3px; }
  .intro-text { left: 313px; top: 626px; width: 280px; font-size: 9.5px; line-height: 18px; color: var(--muted); }
  .intro-photo { left: 607px; top: 614px; width: 178px; height: 92px; background: radial-gradient(ellipse at 40% 60%, #d57f9a 0%, #c6c2d6 35%, #ffffff 70%); }
  .read-more { left: 693px; top: 709px; width: 100px; height: 18px; background: var(--black); color: var(--white); font-family: "Lora", serif; font-size: 8.5px; letter-spacing: .8px; display: grid; place-items: center; clip-path: polygon(0 0,100% 0,94% 50%,100% 100%,0 100%,6% 50%); }
  .col h3 { font-family: "Josefin Sans", sans-serif; font-weight: 400; font-size: 12px; letter-spacing: .3px; color: var(--ink); margin-bottom: 10px; white-space: nowrap; }
  .col p { font-size: 9.5px; line-height: 18px; color: var(--muted); }
  .col-a { left: 307px; top: 750px; width: 236px; }
  .col-b { left: 563px; top: 750px; width: 240px; }

  /* products */
  .latest { left: 137px; top: 904px; width: 399px; }
  .products { left: 160px; top: 943px; display: flex; gap: 27px; }
  .product { width: 102px; }
  .product-photo { width: 102px; height: 100px; border: 4px dotted #c9c9c9; background: radial-gradient(circle at 50% 55%, #e48fa6 0%, #f0dfe4 35%, #fafafa 70%); }
  .product:nth-child(2) .product-photo { background: radial-gradient(circle at 50% 55%, #cfc9d8 0%, #f0eef3 40%, #fafafa 75%); }
  .product:nth-child(3) .product-photo { background: radial-gradient(circle at 50% 45%, #a87a7f 0%, #e6b6c6 35%, #f8f2f4 75%); }
  .product h5 { font-weight: 400; font-size: 9.5px; line-height: 12px; color: var(--ink); margin: 8px 0 0 6px; }
  .product .price { font-size: 9.5px; color: #c33c55; margin-left: 6px; }

  .sales { left: 548px; top: 904px; width: 256px; height: 186px; background: var(--panel); }
  .sales ul { list-style: none; padding: 12px 8px 0 14px; }
  .sales li { display: flex; justify-content: space-between; align-items: center; height: 24px; font-size: 9.5px; color: #666; }
  .sales li b { font-weight: 400; width: 83px; height: 15px; background: var(--black); color: var(--white); font-size: 9.5px; display: grid; place-items: center; clip-path: polygon(0 0,100% 0,95% 50%,100% 100%,0 100%,5% 50%); }

  /* footer */
  .footer { left: 0; top: 1124px; width: 933px; height: 76px; background: linear-gradient(#e9e9e9, #f3f3f3); }
  .footer-links { left: 147px; top: 1144px; display: flex; gap: 12px; font-family: "Lora", serif; font-size: 9px; color: var(--black); }
  .copyright { left: 147px; top: 1163px; font-size: 8.5px; color: #555; }
  .social-foot { left: 471px; top: 1146px; }
  .social-foot span { width: 22px; height: 22px; background: #555; }
  .footer-brand { left: 583px; top: 1140px; font-family: "Playfair Display", serif; font-size: 30px; color: #8e8e8e; }
</style>
</head>
<body>

<header>
  <div class="abs top-band"></div>
  <svg class="abs logo-panel" viewBox="0 0 413 128" aria-hidden="true">
    <path d="M0 0 H413 L392 100 Q387 118 365 118 H48 Q26 118 21 100 Z" fill="#ffffff" stroke="#e2e2e2"/>
  </svg>
  <div class="abs brand">Kupfer und Leinen</div>
  <span class="abs brand-dot"></span>
  <nav class="abs social social-top" aria-label="Soziale Netzwerke"><span></span><span></span><span></span></nav>

  <nav class="abs nav" aria-label="Hauptnavigation">
    <svg width="599" height="40" viewBox="0 0 599 40" aria-hidden="true">
      <path d="M12 1 H587 L598 20 L587 39 H12 L1 20 Z" fill="#ffffff" stroke="#cfcfcf"/>
      <path d="M16 4 H583 L592 20 L583 36 H16 L7 20 Z" fill="#fafafa" stroke="#e4e4e4"/>
    </svg>
    <ul>
      <li class="active">MODE</li>
      <li>SCHMUCK</li>
      <li>SHOP</li>
      <li>VIDEO</li>
      <li>REFERENZEN</li>
      <li>KONTAKT</li>
      <li>FRÜHLINGSERWACHEN</li>
    </ul>
  </nav>
</header>

<main>
  <section class="abs slider">
    <div class="slide-photo" role="img" aria-label="Model mit Perlenkette neben einem Armband aus rosa Glasperlen und Silberkugeln"></div>
    <div class="slide-head">
      <div class="line">EIN GANZ BESONDERES BOUTIQUE,</div>
      <div class="line">WO SCHMUCK UND MODE SIND HANDGEFERTIGT</div>
      <div class="claim">NUR MIT DEN BESTEN MATERIALIEN</div>
    </div>
  </section>
  <svg class="abs slide-arrow prev" viewBox="0 0 22 48" aria-label="Zurück"><path d="M22 0 V48 Q0 44 0 24 Q0 4 22 0Z" fill="#e98aa2"/><path d="M14 17 L8 24 L14 31" stroke="#fff" stroke-width="2.5" fill="none"/></svg>
  <svg class="abs slide-arrow next" viewBox="0 0 22 48" aria-label="Weiter"><path d="M0 0 V48 Q22 44 22 24 Q22 4 0 0Z" fill="#e98aa2"/><path d="M8 17 L14 24 L8 31" stroke="#fff" stroke-width="2.5" fill="none"/></svg>
  <div class="abs dots"><span></span><span></span><span></span><span></span><span></span></div>

  <aside class="abs sidebar">
    <div class="box-head dark">CATEGORIES <i><svg width="7" height="8" viewBox="0 0 7 8"><path d="M0 0 L7 4 L0 8Z" fill="#4a4a4a"/></svg></i></div>
    <div class="cat-group">
      <h4>Mode</h4>
      <ul>
        <li>Brautkleid</li><li>Abendkleid</li><li>Cocktailkleid</li><li>Etuikleid</li><li>Businesskostüm</li><li>Mantel</li><li>Bluse</li><li>Rock</li><li>Sommerkleid</li>
      </ul>
    </div>
    <div class="cat-group">
      <h4>Schmuck</h4>
      <ul>
        <li>Ohrring</li><li>Anhänger</li><li>Kette</li><li>Ring</li><li>Armband</li><li>Braut-Schmuck</li><li>Referenzen</li>
      </ul>
    </div>
  </aside>

  <div class="abs intro-head">
    <h1 class="intro-title">KUPFER UND LEINEN</h1>
    <p class="intro-lead">is a very special boutique where jewelry and fashion are hand-crafted – using only the finest materials.</p>
  </div>
  <p class="abs intro-text">In 2009, two designers opened the boutique „Kupfer und Leinen" in Düsseldorf Unterbilk. Since then, they are enriching the fashion world in Düsseldorf with their creativity. Already now, their little fashion and jewelry paradise has found its steady fan base.</p>
  <div class="abs intro-photo" role="img" aria-label="Ohrringe mit rosa Glastropfen"></div>
  <a class="abs read-more" href="#">READ MORE</a>

  <article class="abs col col-a">
    <h3>STYLING, WHERE EVERY DETAILS FITS</h3>
    <p>The clou: both designers work closely together and align their creations – there is always a matching piece of jewelry to suit the dresses. For wedding and evening gowns, you will even find hair needles.</p>
  </article>
  <article class="abs col col-b">
    <h3>YOUR DREAM – OUR PASSION</h3>
    <p>By the way, customers having their own ideas are very welcome: At „Kupfer und Leinen", real experts are working, so they can make almost any wish come true … so, just choose from the available treasures – or order an individual piece of jewelry for your dress.</p>
  </article>

  <section class="abs latest">
    <div class="box-head light">LATEST PRODUCTS <i><svg width="7" height="8" viewBox="0 0 7 8"><path d="M0 0 L7 4 L0 8Z" fill="#ffffff"/></svg></i></div>
  </section>
  <div class="abs products">
    <div class="product">
      <div class="product-photo" role="img" aria-label="Ohrringe mit rosa Perlen"></div>
      <h5>Unser Nikolausgeschenk für euch -</h5><div class="price">€ 69</div>
    </div>
    <div class="product">
      <div class="product-photo" role="img" aria-label="Zarte Kette mit hellen Perlen"></div>
      <h5>Unser Nikolausgeschenk für euch -</h5><div class="price">€ 69</div>
    </div>
    <div class="product">
      <div class="product-photo" role="img" aria-label="Geschenkbox mit rosa Schleife"></div>
      <h5>Unser Nikolausgeschenk für euch -</h5><div class="price">€ 69</div>
    </div>
  </div>

  <section class="abs sales">
    <div class="box-head dark">SALES ITEMS <i><svg width="7" height="8" viewBox="0 0 7 8"><path d="M0 0 L7 4 L0 8Z" fill="#4a4a4a"/></svg></i></div>
    <ul>
      <li>Türkise Kette aus 925er Silber <b>Save € 50</b></li>
      <li>Türkise Kette aus 925er Silber <b>Save € 46</b></li>
      <li>Türkise Kette aus 925er Silber <b>Save € 24,45</b></li>
      <li>Türkise Kette aus 925er Silber <b>Save € 2</b></li>
      <li>Türkise Kette aus 925er Silber <b>Save € 2</b></li>
      <li>Türkise Kette aus 925er Silber <b>Save € 2</b></li>
    </ul>
  </section>
</main>

<footer>
  <div class="abs footer"></div>
  <nav class="abs footer-links"><a href="#">Terms &amp; conditions</a><a href="#">Privacy policy</a><a href="#">Sitemap</a></nav>
  <p class="abs copyright">Copyright © 2013 KupferLeinen.com All rights reserved!</p>
  <div class="abs social social-foot"><span></span><span></span><span></span></div>
  <div class="abs footer-brand">Kupfer und Leinen</div>
</footer>

</body>
</html>
```